Kestrelwood Pathways Agency business cards

Australian company about to start offering its services. We recruit international students to come to study English, vocational education and postgraduate courses in Australia. We help them find the institution and select the right city they want to come to Australia. We are a young, online oriented and supportive agency. Our clients are between 18 and 35 years old, mainly University students, young professionals or people with work experience. We provide much more information that any other agency offer. We administrate a Facebook group with more than 11.000 members that daily ask questions about general information when coming to Australia, while they are here and even after they leave the country

Target Market(s)

International students from South America, Central America and Europe

Industry/Entity Type

Student

Contact Information for Business Card

Tomas Brevik
Managing Director
tomas@velmorin.com.au
www.velmorin.com.au
+61 491058263
Melbourne, Australia

Font styles to use
Serif
Sans Serif

Colors

Designer to choose colors to be used in the design.

Requirements
Must have
• Horizontal design
• Standard business card size and shape. If font uses green or yellow colours, they will have to match the ones from the logo
Nice to have
• UPDATE: Use the contents of the green image to design one of the card sides. Use our logo in the background of that side as watermark.
• Passport image, or immigration stamps. A picture of the Yarra River (from Melbourne) would be cool as well.
Should not have
• Non-standard business card size and shape
• Not black as the background colour of any sides as we are not a VIP agency or a hight class service. We are orientes to young people and they like colours, pictures, something attractive.
• Vertical design
• NO YELLOW or BLACK AS THE BACKGROUND COLOUR OF ANY SIDE OF THE BIZ CARD

```html
<!DOCTYPE html>
<html lang="en">
<head>
<meta charset="utf-8">
<title>Kestrelwood Pathways Agency – Business Cards</title>
<link href="https://fonts.googleapis.com/css2?family=Roboto:wght@400;500;700&display=swap" rel="stylesheet">
<style>
  :root {
    --page-bg: #e6e7e8;
    --brand-green: #075e3c;
    --brand-green-light: #0a6a43;
    --brand-yellow: #e5bb22;
    --card-white: #ffffff;
    --text-grey: #3a3a3a;
    --mark-silver: #d9dcdb;
  }
  * { margin: 0; padding: 0; box-sizing: border-box; }
  html, body { width: 1200px; height: 1200px; overflow: hidden; }
  body {
    background: var(--page-bg);
    font-family: "Roboto", Arial, sans-serif;
    position: relative;
  }
  .card {
    position: absolute;
    left: 180px;
    width: 840px;
    height: 480px;
    box-shadow: 0 10px 30px rgba(0,0,0,0.18);
  }
  /* Back side */
  .card--back {
    top: 90px;
    background: linear-gradient(135deg, var(--brand-green) 0%, var(--brand-green-light) 100%);
    display: flex;
    align-items: center;
    justify-content: center;
  }
  .wordmark {
    display: flex;
    align-items: center;
    gap: 16px;
    font-weight: 700;
    letter-spacing: 0.5px;
  }
  .wordmark__dot {
    width: 22px; height: 22px; border-radius: 50%;
  }
  .card--back .wordmark { font-size: 58px; color: var(--mark-silver); }
  .card--back .wordmark__dot { background: var(--mark-silver); }

  /* Front side */
  .card--front {
    top: 630px;
    background: var(--card-white);
  }
  .accent-bar {
    position: absolute;
    left: 0; top: 40px;
    width: 22px; height: 46px;
    background: var(--brand-yellow);
  }
  .holder {
    position: absolute;
    left: 56px; top: 36px;
  }
  .holder__name {
    font-size: 31px; font-weight: 700;
    color: var(--brand-green);
    line-height: 1.1;
  }
  .holder__role {
    font-size: 18px; font-weight: 500;
    color: var(--brand-yellow);
    margin-top: 2px;
  }
  .card--front .wordmark {
    position: absolute;
    right: 70px; top: 150px;
    font-size: 52px; color: var(--brand-green);
  }
  .card--front .wordmark__dot { background: var(--brand-yellow); }
  .contact {
    position: absolute;
    left: 56px; top: 300px;
    list-style: none;
  }
  .contact__item {
    display: flex; align-items: center; gap: 14px;
    font-size: 20px; color: var(--brand-green);
    height: 30px;
  }
  .contact__icon {
    width: 22px; height: 22px;
    background: var(--brand-green);
    border-radius: 5px;
    display: flex; align-items: center; justify-content: center;
  }
  .location {
    position: absolute;
    right: 80px; bottom: 40px;
    font-size: 21px; color: var(--text-grey);
  }
</style>
</head>
<body>
  <section class="card card--back" aria-label="Card back">
    <div class="wordmark"><span class="wordmark__dot"></span><span>Kestrelwood</span></div>
  </section>

  <section class="card card--front" aria-label="Card front">
    <div class="accent-bar"></div>
    <div class="holder">
      <p class="holder__name">Tomas Brevik</p>
      <p class="holder__role">Managing Director</p>
    </div>

    <div class="wordmark"><span class="wordmark__dot"></span><span>Kestrelwood</span></div>

    <ul class="contact">
      <li class="contact__item">
        <span class="contact__icon">
          <svg width="14" height="14" viewBox="0 0 14 14"><path d="M3 1.5 L5 1.5 L6 4.5 L4.6 5.5 Q5.8 8.2 8.5 9.4 L9.5 8 L12.5 9 L12.5 11 Q12.5 12.5 11 12.5 Q2 12 1.5 3 Q1.5 1.5 3 1.5 Z" fill="#fff"/></svg>
        </span>+61 491058263
      </li>
      <li class="contact__item">
        <span class="contact__icon">
          <svg width="14" height="14" viewBox="0 0 14 14"><rect x="1.5" y="3" width="11" height="8" fill="none" stroke="#fff" stroke-width="1.3"/><path d="M1.5 3 L7 7.5 L12.5 3" fill="none" stroke="#fff" stroke-width="1.3"/></svg>
        </span>tomas@velmorin.com.au
      </li>
      <li class="contact__item">
        <span class="contact__icon">
          <svg width="14" height="14" viewBox="0 0 14 14" fill="none" stroke="#fff" stroke-width="1.1"><circle cx="7" cy="7" r="5.5"/><ellipse cx="7" cy="7" rx="2.4" ry="5.5"/><path d="M1.5 7 H12.5 M2.4 4 H11.6 M2.4 10 H11.6"/></svg>
        </span>www.velmorin.com.au
      </li>
    </ul>

    <p class="location">Melbourne, Australia</p>
  </section>
</body>
</html>
```